Plastic Aesthetic and Reconstructive Surgery

I need a double sided luxurius Business Card, with a minimal, modern design focused on my job.
Besides my Name, Surname and contact information, the use of my initials (M and T) in free style combination as a logo will help.
In the one side all data written in English.
In the other side written in Greek if possible.
Please feel free to use the letter type and size you prefer.
Please use icons type and size and orientation you like.
The Name, Surname, occupation and the initials can be UV spotted.
You can use also in the background a texture or something that will make the card luxurious.
I would prefer pal colors.
Each side can have different colors or even better they can be reversed or inverted
As I have said you can use the wet sand color, light brown, dark brown, gold, light gold, white
Updates

Need extra days to review

i am waiting for some new ideas and some modifications from the designers. I need a couple of days extention of the period for the designers to post their modifications.

Target Market(s)

Patients who need a reconstructive intervention or surgery. Also people, mainly women, that they need aesthetic or cosmetic interventions to face or body

Contact Information for Business Card

Name and surname, occupation, member of an organization , mobile telephone number, Mail, Facebook and Instagram accounts

Font styles to use
Script
Other font styles liked:
• Gabriola

Colors
FFC000
F8CF3A
FAE287
FDF2CF
FEFAEE

Requirements
Must have
• A free combination of my initials (M and T) as a logo
Nice to have
• Fade out with the background colors, UV spotted of the name, initials logo
Should not have
• Address

```html
<!DOCTYPE html>
<html lang="en">
<head>
<meta charset="utf-8">
<title>Markos Theodorou – Business Card</title>
<link rel="stylesheet" href="https://fonts.googleapis.com/css2?family=Cormorant+Garamond:ital,wght@0,500;0,600;1,500&family=Montserrat:wght@500&display=swap">
<style>
  :root {
    --backdrop: #1c1c20;
    --kraft: #b68c62;
    --kraft-light: #c29a70;
    --kraft-mark: rgba(120, 88, 58, 0.35);
    --paper: #ffffff;
    --paper-mark: #ebebeb;
    --ink: #111111;
    --ink-soft: #8a8a8a;
    --gold: #f0b400;
  }
  * { box-sizing: border-box; margin: 0; padding: 0; }
  html, body { width: 1200px; height: 800px; overflow: hidden; }
  body {
    background: var(--backdrop);
    position: relative;
    font-family: "Montserrat", Arial, sans-serif;
  }
  .card {
    position: absolute;
    top: 225px;
    width: 540px;
    height: 350px;
    border-radius: 26px;
    overflow: hidden;
  }
  .card--english { left: 40px; background: linear-gradient(135deg, var(--kraft-light), var(--kraft)); }
  .card--greek { left: 620px; background: var(--paper); }

  .monogram {
    font-family: "Cormorant Garamond", Georgia, serif;
    font-weight: 600;
    line-height: 1;
    letter-spacing: -0.04em;
    position: absolute;
  }
  .card--english .monogram--faint { font-size: 250px; color: var(--kraft-mark); left: 95px; top: 40px; }
  .card--english .monogram--main { font-size: 84px; color: var(--ink); left: 200px; top: 72px; }
  .card--english .name {
    position: absolute; left: 0; right: 0; top: 188px; text-align: center;
    font-size: 17px; font-weight: 500; letter-spacing: 0.02em; color: var(--ink);
  }
  .card--english .specialty {
    position: absolute; left: 0; right: 0; top: 216px; text-align: center;
    font-family: "Cormorant Garamond", Georgia, serif; font-style: italic;
    font-size: 17px; color: #2a2118;
  }

  .card--greek .monogram--faint { font-size: 210px; color: var(--paper-mark); right: 50px; top: 20px; }
  .card--greek .monogram--main { font-size: 60px; color: var(--ink); left: 40px; top: 40px; }
  .handle {
    position: absolute; right: 34px; top: 178px;
    display: flex; align-items: center; gap: 6px;
    font-size: 13px; color: var(--ink);
  }
  .handle-dot { width: 12px; height: 12px; border: 1.5px solid var(--ink); border-radius: 50%; }
  .details { position: absolute; left: 40px; bottom: 34px; }
  .details .name { font-size: 16px; font-weight: 500; color: var(--ink); letter-spacing: 0.01em; }
  .details .role {
    font-family: "Cormorant Garamond", Georgia, serif; font-style: italic;
    font-size: 15px; color: var(--ink-soft); line-height: 1.25; margin-top: 4px;
  }
  .contact { list-style: none; margin-top: 10px; font-size: 13px; color: var(--ink); }
  .contact li { display: flex; align-items: center; gap: 6px; margin-top: 5px; }
  .contact svg { width: 13px; height: 13px; }
  .messenger-dot { width: 11px; height: 11px; border: 1.5px solid var(--gold); border-radius: 50%; }
</style>
</head>
<body>
  <section class="card card--english" aria-label="Card front, English">
    <div class="monogram monogram--faint" aria-hidden="true">MT</div>
    <div class="monogram monogram--main">MT</div>
    <p class="name">MARKOS THEODOROU, MD, MSc</p>
    <p class="specialty">Plastic Reconstructive and Aesthetic Surgery</p>
  </section>

  <section class="card card--greek" aria-label="Card back, Greek">
    <div class="monogram monogram--faint" aria-hidden="true">MT</div>
    <div class="monogram monogram--main">MT</div>
    <div class="handle"><span class="handle-dot"></span>drmtheo</div>
    <div class="details">
      <p class="name">ΜΑΡΚΟΣ ΘΕΟΔΩΡΟΥ, MD, MSc</p>
      <p class="role">Αισθητική και Επανορθωτική Πλαστική Χειρουργική<br>Μέλος Ε.Π.Χ.Ε.Α</p>
      <ul class="contact">
        <li>
          <svg viewBox="0 0 24 24" aria-hidden="true"><path fill="var(--gold)" d="M6.6 10.8a15 15 0 0 0 6.6 6.6l2.2-2.2a1 1 0 0 1 1-.25 11.4 11.4 0 0 0 3.6.57 1 1 0 0 1 1 1V20a1 1 0 0 1-1 1A17 17 0 0 1 3 4a1 1 0 0 1 1-1h3.5a1 1 0 0 1 1 1c0 1.25.2 2.45.57 3.6a1 1 0 0 1-.25 1z"/></svg>
          <span class="messenger-dot"></span><span class="messenger-dot"></span>
          +30 694 210 3865
        </li>
        <li>
          <svg viewBox="0 0 24 24" aria-hidden="true"><rect x="2" y="5" width="20" height="14" rx="1.5" fill="var(--gold)"/><path d="M3 6l9 7 9-7" fill="none" stroke="#fff" stroke-width="1.6"/></svg>
          markos.theodorou@mailbox.gr
        </li>
      </ul>
    </div>
  </section>
</body>
</html>
```